New Business Card Design Project

Updated business card design. I am moving towards more coaching of, for the most part women, who are searching for more in their lives. I am an intuitive healer, homeopath and nutritionist but also an author and motivational speaker. Int the past I have included my photo on the card but that is not essential. My book is called the Brilliance of Saffron - Reclaiming the Shade of Your Spirit so my colours are typically magenta.
Target Market(s)
Women - 35 - 60 considering improving their health. However, I am also a professional speaker with a target audience including corporate and conferences.
Industry/Entity Type
Health And Wellness
Contact Information for Business Card
Lucinda Parvell, ND, CNP, BSc
www.lucindaparvell.com
lucinda@lucindaparvell.com
519-362-7015
Facebook, instagram and twitter logos
Look and feel
Each slider illustrates characteristics of the customer's brand and the style your logo design should communicate.

```html
<!DOCTYPE html>
<html lang="en">
<head>
<meta charset="utf-8">
<title>Lucinda Parvell – Business Card</title>
<link rel="stylesheet" href="https://fonts.googleapis.com/css2?family=Josefin+Sans:wght@300;400&family=Montserrat:wght@400;700&display=swap">
<style>
  :root {
    --backdrop: #d6d6d6;
    --card-paper: #f1f1f0;
    --ink: #2b2b2b;
    --ink-soft: #4a4a4a;
    --magenta: #d1246f;
    --magenta-deep: #c81f66;
    --magenta-soft: #dc4a85;
    --rule: #c9c9c9;
    --white: #ffffff;
  }
  * { box-sizing: border-box; margin: 0; padding: 0; }
  html, body { width: 1200px; height: 1016px; overflow: hidden; }
  body { background: var(--backdrop); position: relative; font-family: "Montserrat", sans-serif; }

  .card {
    position: absolute; left: 180px; width: 840px; height: 468px;
    box-shadow: 0 6px 18px rgba(0,0,0,.18);
    overflow: hidden;
  }
  .card--front { top: 26px; background: var(--card-paper); }
  .card--back { top: 522px; background: var(--magenta); }

  /* front: brand block */
  .brand { position: absolute; left: 60px; top: 100px; width: 370px; text-align: center; }
  .brand__name {
    font-family: "Josefin Sans", sans-serif; font-weight: 300;
    font-size: 54px; line-height: 1.05; color: var(--ink);
    display: inline-flex; align-items: center; gap: 14px;
  }
  .brand__name span { display: block; text-align: left; }
  .brand__mark { width: 52px; height: 52px; border-radius: 50%; background: var(--magenta); flex: none; }
  .tagline {
    font-family: "Josefin Sans", sans-serif; font-weight: 300;
    font-size: 25px; color: var(--ink-soft); margin-top: 44px; letter-spacing: .5px;
    white-space: nowrap;
  }
  .tagline__dot { color: var(--magenta); padding: 0 10px; }

  .divider { position: absolute; left: 441px; top: 132px; width: 1px; height: 220px; background: var(--rule); }

  /* front: contact block */
  .contact { position: absolute; left: 481px; top: 128px; color: var(--ink); }
  .contact__name { font-weight: 700; font-size: 28px; letter-spacing: .2px; }
  .contact__creds { font-size: 18px; color: var(--ink-soft); margin-top: 2px; }
  .contact__list { list-style: none; margin-top: 36px; }
  .contact__item { display: flex; align-items: center; gap: 12px; font-size: 17.5px; height: 27px; color: var(--ink-soft); white-space: nowrap; }
  .contact__icon { width: 18px; height: 18px; flex: none; }
  .social { display: flex; align-items: center; gap: 6px; margin-top: 24px; font-size: 17.5px; color: var(--ink-soft); }
  .social__dot { width: 17px; height: 17px; border-radius: 50%; background: var(--magenta); }
  .social__handle { margin-left: 8px; }

  /* back */
  .back-pattern {
    position: absolute; inset: 0;
    background: radial-gradient(ellipse at 50% 45%, var(--magenta-soft) 0%, var(--magenta) 55%, var(--magenta-deep) 100%);
  }
  .back-brand { position: absolute; left: 0; right: 0; top: 150px; text-align: center; color: var(--white); }
  .back-brand__name {
    font-family: "Josefin Sans", sans-serif; font-weight: 300;
    font-size: 76px; line-height: 1; display: inline-flex; align-items: center; gap: 20px;
  }
  .back-brand__mark { width: 62px; height: 62px; border-radius: 50%; background: var(--white); flex: none; }
  .back-brand .tagline { color: var(--white); font-size: 28px; margin-top: 34px; }
  .back-brand .tagline__dot { color: var(--white); }
</style>
</head>
<body>

<section class="card card--front" aria-label="Card front">
  <div class="brand">
    <div class="brand__name"><span>Lucinda<br>Parvell</span><i class="brand__mark"></i></div>
    <p class="tagline"><span class="tagline__dot">•</span>vitality maverick<span class="tagline__dot">•</span></p>
  </div>

  <div class="divider"></div>

  <div class="contact">
    <h1 class="contact__name">Lucinda Parvell</h1>
    <p class="contact__creds">ND, CNP, BSc</p>
    <ul class="contact__list">
      <li class="contact__item">
        <svg class="contact__icon" viewBox="0 0 24 24" aria-hidden="true"><path fill="var(--magenta)" d="M6.6 10.8a15.1 15.1 0 0 0 6.6 6.6l2.2-2.2a1 1 0 0 1 1-.25 11.4 11.4 0 0 0 3.6.57 1 1 0 0 1 1 1V20a1 1 0 0 1-1 1A17 17 0 0 1 3 4a1 1 0 0 1 1-1h3.5a1 1 0 0 1 1 1c0 1.25.2 2.45.57 3.57a1 1 0 0 1-.25 1z"/></svg>
        519-362-7015
      </li>
      <li class="contact__item">
        <svg class="contact__icon" viewBox="0 0 24 24" aria-hidden="true"><rect x="3" y="5.5" width="18" height="13" fill="none" stroke="var(--magenta)" stroke-width="1.8"/><path d="M3.5 6.5l8.5 6.5 8.5-6.5" fill="none" stroke="var(--magenta)" stroke-width="1.8"/></svg>
        lucinda@lucindaparvell.com
      </li>
      <li class="contact__item">
        <svg class="contact__icon" viewBox="0 0 24 24" aria-hidden="true"><g fill="none" stroke="var(--magenta)" stroke-width="1.6"><circle cx="12" cy="12" r="9"/><ellipse cx="12" cy="12" rx="4" ry="9"/><path d="M3 12h18M4.5 7.5h15M4.5 16.5h15"/></g></svg>
        www.lucindaparvell.com
      </li>
    </ul>
    <div class="social">
      <i class="social__dot"></i><i class="social__dot"></i><i class="social__dot"></i>
      <span class="social__handle">@LucindaParvell</span>
    </div>
  </div>
</section>

<section class="card card--back" aria-label="Card back">
  <div class="back-pattern" role="img" aria-label="Soft magenta swirl pattern covering the card"></div>
  <div class="back-brand">
    <div class="back-brand__name"><i class="back-brand__mark"></i>Lucinda Parvell</div>
    <p class="tagline"><span class="tagline__dot">•</span>vitality maverick<span class="tagline__dot">•</span></p>
  </div>
</section>

</body>
</html>
```